Worksheet for a seminar - wheel of wellbeing

I need a 1 page worksheet for a course I am running next week.
1. The worksheet is based is designed to tie into Valdoric who use 4 colours per specific quadrants - Blue top left, Yellow top right, Green bottom left, Red bottom right. As this is designed to be written and to be printed, it may need to be pale colours however I am open to the correct colours with the image on top if necessary

2. The wellbeing wheel needs to be a design of it's own as it will be used in other things. I would like to have a format for the base wheel that can be changed by me (Only the title names)

3. I have provided the 2 business logo's - these down need to be too big

I hope this helps.

Target Market(s)

Corporate managers and staff - worksheet being used in a workshop

Industry/Entity Type

Wheel

Colors

Designer to choose colors to be used in the design.

Requirements
Must have
• A professional looking wheel that can be used for other purposes. I want to be able to change the 'pie' titles. I will also require a A4 size of the wheel with blank spaces for titles
Nice to have
• A modern feel

```html
<!DOCTYPE html>
<html lang="en">
<head>
<meta charset="utf-8">
<title>Wheel of Well being – Worksheet</title>
<link rel="stylesheet" href="https://fonts.googleapis.com/css2?family=Source+Sans+3:wght@300;400;700;900&family=Oswald:wght@600&family=Tinos&display=swap">
<style>
  :root {
    --header-green: #066b3a;
    --title-yellow: #fff200;
    --cream: #fefce3;
    --ink: #1a1a1a;
    --purple: #7d3f98;
    --pink: #ee4b8b;
    --rule: #3a3a3a;
    --seg-yellow: #fdf2bd;
    --seg-green: #dfebc8;
    --seg-peach: #fbd3c0;
    --seg-mint: #b3d6c4;
    --seg-rose: #ecc1c3;
    --seg-lilac: #dcbad8;
    --seg-beige: #ded6cb;
    --seg-blue: #b5e2f7;
    --tab-yellow: #fbbc1a;
    --tab-green: #8dc63f;
    --tab-orange: #f26522;
    --tab-forest: #147040;
    --tab-red: #c8202f;
    --tab-purple: #92278f;
    --tab-brown: #8b6a46;
    --tab-blue: #29a8e0;
  }
  * { margin: 0; padding: 0; box-sizing: border-box; }
  html, body { width: 848px; height: 1200px; overflow: hidden; background: #fff; }
  body { font-family: "Source Sans 3", sans-serif; color: var(--ink); }
  .sheet { position: relative; width: 848px; height: 1200px; background: #fff; }
  .masthead { position: absolute; left: 0; top: 0; width: 848px; height: 170px; background: var(--header-green); text-align: center; color: var(--title-yellow); }
  .masthead h1 { font-weight: 900; font-size: 58px; letter-spacing: -1px; line-height: 1; padding-top: 44px; }
  .masthead p { font-weight: 300; font-size: 42px; line-height: 1; margin-top: 2px; }
  .wheel-zone { position: absolute; left: 0; top: 170px; width: 848px; height: 412px; background: var(--cream); }
  .step-title { position: absolute; font-weight: 700; font-size: 28px; line-height: 1; }
  .step-sub { position: absolute; font-weight: 300; font-size: 18px; line-height: 1; }
  .date-label { position: absolute; font-size: 18px; line-height: 1; }
  .wheel { position: absolute; left: 0; top: 0; }
  .tab-label { font-family: "Oswald", sans-serif; font-weight: 600; font-size: 12px; fill: #fff; }
  .band { position: absolute; top: 582px; height: 64px; color: #fff; font-weight: 700; font-size: 24px; padding-left: 18px; line-height: 64px; }
  .band--action { left: 35px; width: 389px; background: var(--purple); padding-top: 6px; }
  .band--reflect { left: 424px; width: 390px; background: var(--pink); }
  .col-label, .question { position: absolute; font-weight: 300; font-size: 16px; line-height: 17px; }
  .action-row { position: absolute; left: 64px; width: 351px; height: 116px; border: 1px solid var(--rule); }
  .action-row .when { position: absolute; left: 281px; top: 0; bottom: 0; border-left: 1px solid var(--rule); }
  .row-num { position: absolute; left: 37px; width: 27px; height: 27px; border: 2px solid var(--ink); background: #fff; font-family: "Tinos", serif; font-size: 20px; text-align: center; line-height: 23px; }
  .answer-box { position: absolute; border: 1px solid var(--rule); }
</style>
</head>
<body>
<main class="sheet">
  <header class="masthead">
    <h1>Wheel of Well being</h1>
    <p>a whole brain approch</p>
  </header>

  <section class="wheel-zone">
    <h2 class="step-title" style="left:40px; top:20px;">1. Assess</h2>
    <p class="step-sub" style="left:40px; top:46px;">Where are you now?</p>
    <h2 class="step-title" style="left:442px; top:24px;">3. Outcomes | Goals</h2>
    <p class="step-sub" style="left:442px; top:50px;">Where do you want to be ?</p>
    <p class="date-label" style="left:32px; top:374px;">Date</p>
    <p class="date-label" style="left:442px; top:374px;">Date achieved by:</p>

    <svg class="wheel" width="848" height="412" viewBox="0 170 848 412" aria-label="Wellbeing wheels">
      <defs>
        <path id="wedge" d="M0 0 L0 -137 A137 137 0 0 1 96.87 -96.87 Z"/>
        <path id="tab" d="M12.99 -148.43 A149 149 0 0 1 95.78 -114.14"/>
        <path id="label-cw" d="M-7.54 -143.80 A144 144 0 0 1 107.01 -96.36"/>
        <path id="label-ccw" d="M113.70 -102.38 A153 153 0 0 0 -8.01 -152.79"/>
      </defs>

      <g class="assess-wheel" transform="translate(230 396)">
        <use href="#wedge" fill="var(--seg-yellow)"/>
        <use href="#wedge" fill="var(--seg-green)" transform="rotate(45)"/>
        <use href="#wedge" fill="var(--seg-peach)" transform="rotate(90)"/>
        <use href="#wedge" fill="var(--seg-mint)" transform="rotate(135)"/>
        <use href="#wedge" fill="var(--seg-rose)" transform="rotate(180)"/>
        <use href="#wedge" fill="var(--seg-lilac)" transform="rotate(225)"/>
        <use href="#wedge" fill="var(--seg-beige)" transform="rotate(270)"/>
        <use href="#wedge" fill="var(--seg-blue)" transform="rotate(315)"/>
        <circle r="138" fill="none" stroke="#fff" stroke-width="3"/>

        <g fill="none" stroke-width="22" stroke-linecap="round">
          <use href="#tab" stroke="var(--tab-yellow)"/>
          <use href="#tab" stroke="var(--tab-green)" transform="rotate(45)"/>
          <use href="#tab" stroke="var(--tab-orange)" transform="rotate(90)"/>
          <use href="#tab" stroke="var(--tab-forest)" transform="rotate(135)"/>
          <use href="#tab" stroke="var(--tab-red)" transform="rotate(180)"/>
          <use href="#tab" stroke="var(--tab-purple)" transform="rotate(225)"/>
          <use href="#tab" stroke="var(--tab-brown)" transform="rotate(270)"/>
          <use href="#tab" stroke="var(--tab-blue)" transform="rotate(315)"/>
        </g>

        <g class="tab-labels" text-anchor="middle">
          <text class="tab-label" style="font-size:11px"><textPath href="#label-cw" startOffset="50%">Business Career Study</textPath></text>
          <text class="tab-label" transform="rotate(45)"><textPath href="#label-cw" startOffset="50%">Physical Health</textPath></text>
          <text class="tab-label" transform="rotate(90)"><textPath href="#label-cw" startOffset="50%">Emotional Health</textPath></text>
          <text class="tab-label" transform="rotate(135)"><textPath href="#label-ccw" startOffset="50%">Spritual</textPath></text>
          <text class="tab-label" transform="rotate(180)"><textPath href="#label-ccw" startOffset="50%">Lovel Relationship</textPath></text>
          <text class="tab-label" transform="rotate(225)"><textPath href="#label-ccw" startOffset="50%">Family</textPath></text>
          <text class="tab-label" transform="rotate(270)"><textPath href="#label-cw" startOffset="50%">Social</textPath></text>
          <text class="tab-label" transform="rotate(315)"><textPath href="#label-cw" startOffset="50%">Personal Growth</textPath></text>
        </g>
      </g>

      <g class="goal-wheel" transform="translate(613 386) scale(0.993)">
        <use href="#wedge" fill="var(--seg-yellow)"/>
        <use href="#wedge" fill="var(--seg-green)" transform="rotate(45)"/>
        <use href="#wedge" fill="var(--seg-peach)" transform="rotate(90)"/>
        <use href="#wedge" fill="var(--seg-mint)" transform="rotate(135)"/>
        <use href="#wedge" fill="var(--seg-rose)" transform="rotate(180)"/>
        <use href="#wedge" fill="var(--seg-lilac)" transform="rotate(225)"/>
        <use href="#wedge" fill="var(--seg-beige)" transform="rotate(270)"/>
        <use href="#wedge" fill="var(--seg-blue)" transform="rotate(315)"/>
      </g>
    </svg>
  </section>

  <h2 class="band band--action">4. Action Plan</h2>
  <h2 class="band band--reflect">2. Refelect</h2>

  <section class="action-plan">
    <span class="col-label" style="left:81px; top:649px;">Action</span>
    <span class="col-label" style="left:352px; top:649px;">When</span>
    <div class="action-row" style="top:676px;"><span class="when"></span></div>
    <div class="row-num" style="top:676px;">1</div>
    <div class="action-row" style="top:802px;"><span class="when"></span></div>
    <div class="row-num" style="top:802px;">2</div>
    <div class="action-row" style="top:927px;"><span class="when"></span></div>
    <div class="row-num" style="top:927px;">3</div>
    <div class="action-row" style="top:1054px;"><span class="when"></span></div>
    <div class="row-num" style="top:1054px;">4</div>
  </section>

  <section class="reflect">
    <p class="question" style="left:436px; top:648px;">Are there any surprises in your wheel?</p>
    <div class="answer-box" style="left:424px; top:676px; width:390px; height:101px;"></div>
    <p class="question" style="left:436px; top:781px;">What wellbeing gaps stand out<br>as being most important</p>
    <div class="answer-box" style="left:424px; top:821px; width:390px; height:87px;"></div>
    <p class="question" style="left:436px; top:917px;">How do you feel about it</p>
    <div class="answer-box" style="left:422px; top:951px; width:393px; height:88px;"></div>
    <p class="question" style="left:436px; top:1045px;">How might this affect your homelife | work | life</p>
    <div class="answer-box" style="left:423px; top:1082px; width:392px; height:87px;"></div>
  </section>
</main>
</body>
</html>
```